tourism marketplace web app redesign*

Hi, I need our front-page redesigned. For the competition please submit a jpg of ABOVE THE FOLD ONLY. The full page redesign will be a revision request. URL is https://qp.trolvexa.hu/hu/index.html login:'fullhd' and password:'asdasd' (Fold is supposed to be at "Kiemelt Ajanlatok", use all elements above that. Please use at least one extra color other than the two in the logo, or you may completely change them. FOCUS should be on the central combined search box (3 dropdown, 2 calendar picker + Kereses Button) just like nestorly.com, ravimoto.com, Pelusi.com, etc... The search box is always large, central, white, we want that too. We want it to look more modern, more clean AND we want to feature a changing beautiful nature photo background (like nestorly.com).Please use our newly designed logo (in attached pdf) and use that new spelling: "ferntrail.online"

```html
<!DOCTYPE html>
<html lang="en">
<head>
<meta charset="utf-8">
<title>Hunting Ground Booking</title>
<link href="https://fonts.googleapis.com/css2?family=Montserrat:wght@400;500;600&display=swap" rel="stylesheet">
<style>
  :root {
    --nav-bg: #262626;
    --nav-text: #ffffff;
    --accent: #0a9a87;
    --panel: #ffffff;
    --field-border: #cfcfcf;
    --field-text: #8a8a8a;
    --tab-text: #7a7a7a;
    --arrow: #777777;
  }
  * { box-sizing: border-box; margin: 0; padding: 0; }
  html, body { width: 1200px; height: 675px; overflow: hidden; }
  body { font-family: "Montserrat", sans-serif; position: relative; background: #6e5a37; }

  .hero-photo {
    position: absolute; inset: 0;
    background:
      radial-gradient(ellipse at 75% 12%, #5d6670 0%, rgba(93,102,112,0) 45%),
      linear-gradient(180deg, #4f5558 0%, #77705c 18%, #a88e55 32%, #9c7c43 55%, #7d6131 78%, #5e4a28 100%);
  }
  .hero-photo::after {
    content: ""; position: absolute; inset: 0;
    background: linear-gradient(90deg, rgba(30,22,12,0.55) 0%, rgba(30,22,12,0) 18%, rgba(30,22,12,0) 85%, rgba(30,22,12,0.25) 100%);
  }

  .site-nav {
    position: absolute; top: 0; left: 0; width: 1200px; height: 40px;
    background: var(--nav-bg); color: var(--nav-text);
    font-size: 12.5px; font-weight: 500;
  }
  .site-nav .brand, .site-nav .nav-link { position: absolute; top: 13px; }
  .partner-button {
    position: absolute; left: 938px; top: 7px; width: 140px; height: 27px;
    background: var(--accent); color: var(--nav-text);
    font-size: 12.5px; font-weight: 500; line-height: 27px; text-align: center;
  }

  .hero-title {
    position: absolute; top: 128px; left: 0; width: 1200px; text-align: center;
    color: #fff; font-size: 28px; font-weight: 500; letter-spacing: 0.2px;
  }
  .hero-subtitle {
    position: absolute; top: 234px; left: 0; width: 1200px; text-align: center;
    color: #fff; font-size: 15px; font-weight: 600; text-transform: uppercase;
  }

  .hunt-tab {
    position: absolute; top: 267px; width: 164px; height: 42px;
    background: var(--panel); color: var(--tab-text);
    font-size: 10px; letter-spacing: 0.3px; text-transform: uppercase;
    display: flex; align-items: center; justify-content: space-between; padding: 0 8px 0 9px;
  }
  .hunt-tab:first-of-type { padding-left: 21px; }
  .check { width: 11px; height: 11px; border: 1px solid #666; border-radius: 2px; flex: none; }

  .search-panel {
    position: absolute; left: 350px; top: 314px; width: 500px; height: 272px;
    background: var(--panel);
  }
  .select-field, .date-field {
    position: absolute; height: 32px; border: 1px solid var(--field-border);
    background: #fff; color: var(--field-text); font-size: 13px;
    line-height: 30px; padding-left: 13px;
  }
  .select-field { left: 19px; width: 463px; }
  .select-field::after {
    content: ""; position: absolute; right: 10px; top: 11px;
    border-left: 5px solid transparent; border-right: 5px solid transparent;
    border-top: 9px solid #6a6a6a;
  }
  .date-field { top: 165px; width: 206px; }
  .swap-icon { position: absolute; left: 278px; top: 169px; }
  .search-button {
    position: absolute; left: 19px; top: 214px; width: 463px; height: 39px;
    background: var(--accent); color: #fff; border-radius: 2px;
    font-size: 14px; font-weight: 500; line-height: 39px; text-align: center;
  }
</style>
</head>
<body>
  <div class="hero-photo" role="img" aria-label="Savanna landscape with acacia tree, tall golden grass and grazing antelope under a stormy sky"></div>

  <nav class="site-nav">
    <span class="brand" style="left:121px">Logo</span>
    <span class="nav-link" style="left:213px">Countries</span>
    <span class="nav-link" style="left:300px">Wild Species</span>
    <span class="nav-link" style="left:406px">About Us</span>
    <span class="nav-link" style="left:490px">Terms &amp; Conditions</span>
    <span class="nav-link" style="left:639px">How it Works</span>
    <span class="partner-button">Become Our Partner</span>
  </nav>

  <h1 class="hero-title">You don't need a hunting organizer!</h1>
  <h2 class="hero-subtitle">Book directly at the hunting ground</h2>

  <div class="hunt-tab" style="left:350px">Individual hunt <span class="check"></span></div>
  <div class="hunt-tab" style="left:518px">Group hunt, shoots, <span class="check"></span></div>
  <div class="hunt-tab" style="left:686px">Exclusive package <span class="check"></span></div>

  <form class="search-panel">
    <div class="select-field" style="top:17px">All Wild</div>
    <div class="select-field" style="top:66px">All Countries</div>
    <div class="select-field" style="top:116px">All Offers</div>
    <div class="date-field" style="left:19px"></div>
    <svg class="swap-icon" width="22" height="24" viewBox="0 0 22 24" fill="none" stroke="var(--arrow)" stroke-width="1.6" stroke-linecap="round" stroke-linejoin="round">
      <path d="M2 7h17M14 2l5 5-5 5"/>
      <path d="M20 17H3M8 12l-5 5 5 5"/>
    </svg>
    <div class="date-field" style="left:275px"></div>
    <div class="search-button">Search</div>
  </form>
</body>
</html>
```